Veltrora

We need a website redesign for a Wordpress-based template. We have WP and Elementor and are looking for a template to modernise the existing website at http://www.veltrora.co.uk. we can handle the relocation of the content but want a new fresh look. As an example, http://quorbix.io looks nice.

```html
<!DOCTYPE html>
<html lang="en">
<head>
<meta charset="utf-8">
<title>Veltrora – Drug Repurposing</title>
<link href="https://fonts.googleapis.com/css2?family=Raleway:ital,wght@0,300;0,400;0,500;0,600;0,700;1,500&display=swap" rel="stylesheet">
<style>
:root{
  --green:#3f9a12;
  --yellow:#f7f200;
  --ink:#2b2b2b;
  --text:#666;
  --panel:#f2f2f2;
  --rule:#cfcfcf;
  --footer:#0a0a0a;
  --white:#fff;
}
*{box-sizing:border-box;margin:0;padding:0}
html,body{width:995px;height:1200px;overflow:hidden;background:var(--white)}
body{position:relative;font-family:"Raleway",sans-serif;color:var(--text)}
.abs{position:absolute}

.site-header{left:0;top:0;width:995px;height:44px;background:linear-gradient(90deg,#a9bd9a 0,#6fa84a 30%,var(--green) 45%)}
.brand{left:191px;top:6px;display:flex;align-items:center;gap:8px;font-size:25px;font-weight:500;color:#3a4a3a}
.brand-dot{width:22px;height:22px;border-radius:50%;background:var(--yellow)}
.social-top{left:789px;top:6px;display:flex;gap:12px}
.social-top span{width:8px;height:8px;border-radius:50%;background:var(--white)}
.main-nav{left:483px;top:24px;display:flex;font-size:8px;font-weight:600;color:var(--white)}
.main-nav a{color:inherit;text-decoration:none;padding:2px 0 9px;margin:0 14px;position:relative}
.main-nav a.active{padding:2px 12px 9px;margin:0 2px;border-bottom:3px solid var(--yellow)}
.main-nav .sep{width:1px;height:9px;background:rgba(255,255,255,.6);margin-top:3px}

.hero{left:0;top:44px;width:995px;height:394px;background:linear-gradient(90deg,#e4e6e8 0,#d7dadd 45%,#c9ced3 65%,#3c68b3 80%,#2f5fae 100%)}
.hero-arrow{top:186px;width:28px;height:65px;background:rgba(150,150,150,.55)}
.hero-arrow svg{position:absolute;left:7px;top:21px}
.hero-title{left:189px;top:146px;font-size:30px;font-weight:700;line-height:37px;color:var(--ink)}
.hero-sub{left:190px;top:225px;font-size:16.5px;line-height:21px;color:var(--ink)}
.btn{display:inline-block;background:var(--yellow);color:#333;font-size:10px;text-align:center}
.hero-btn{left:190px;top:280px;width:103px;height:22px;line-height:22px}
.dots{left:488px;top:419px;display:flex;gap:5px}
.dots span{width:8px;height:8px;border-radius:50%;background:#555;border:1.5px solid #fff}
.dots span.on{background:var(--yellow);border-color:#444}

.mission-title{left:0;width:995px;top:458px;text-align:center;font-size:31px;font-weight:300;color:var(--ink)}
.mission-text{left:240px;width:515px;top:503px;text-align:center;font-size:11.5px;line-height:16px}

.feature{left:173px;width:649px;background:var(--panel)}
.photo{position:absolute;width:324px}
.feature h2{position:absolute;font-size:16px;font-weight:600;color:#111}
.feature p{position:absolute;font-size:9.3px;line-height:14px}
.track{top:568px;height:147px}
.track .photo{left:0;top:0;height:147px;background:linear-gradient(90deg,#e2d6c6,#b89a7c 40%,#d9b9c4 60%,#c9a98a)}
.services{top:723px;height:178px}
.services .photo{left:325px;top:0;height:178px;background:linear-gradient(135deg,#e6e2dc,#d7703c 35%,#f1efe9 55%,#2f5647 75%,#ece9e2)}

.book-box{left:172px;top:925px;width:90px;height:132px;background:var(--panel);text-align:center}
.book-box h3{margin-top:13px;font-size:11px;font-weight:500;color:#333}
.book-cover{position:absolute;left:19px;top:33px;width:52px;height:77px;background:linear-gradient(180deg,#5e88c9,#e8eef6 45%,#f5f7fa);border:1px solid #999}
.reviews{left:271px;top:922px;width:551px}
.review{border-bottom:1px solid var(--rule);font-size:9.5px;line-height:14px}
.review cite{display:block;font-size:7px;font-weight:500;font-style:italic;color:#222}
.r1{height:37px}
.r2{height:50px;padding-top:12px}
.r3{height:49px;padding-top:11px}
.review cite{margin-top:3px}

.social-bar{left:0;top:1101px;width:995px;height:31px;background:var(--green);color:var(--white);font-size:10px;font-weight:600}
.social-bar .label{position:absolute;left:173px;top:9px;display:flex;align-items:center;gap:12px}
.social-bar .label i{width:7px;height:7px;border-radius:50%;background:var(--white);display:inline-block}
.social-bar .contact{position:absolute;right:174px;top:9px}
.site-footer{left:0;top:1132px;width:995px;height:68px;background:var(--footer);color:#bbb;font-size:6px;text-align:center;line-height:10px;padding-top:20px}
</style>
</head>
<body>
<header class="abs site-header">
  <div class="abs brand">Veltrora <span class="brand-dot"></span></div>
  <div class="abs social-top"><span></span><span></span></div>
  <nav class="abs main-nav">
    <a class="active" href="#">Home</a><span class="sep"></span>
    <a href="#">About</a><span class="sep"></span>
    <a href="#">Therapeutic Switching</a><span class="sep"></span>
    <a href="#">Services</a><span class="sep"></span>
    <a href="#">Blog</a><span class="sep"></span>
    <a href="#">Contact</a>
  </nav>
</header>

<section class="abs hero" role="img" aria-label="Surgeon in blue scrubs in a bright operating theatre"></section>
<div class="abs hero-arrow" style="left:0"><svg width="12" height="22"><path d="M10 1 L2 11 L10 21" fill="none" stroke="#fff" stroke-width="1.5"/></svg></div>
<div class="abs hero-arrow" style="left:967px"><svg width="12" height="22"><path d="M2 1 L10 11 L2 21" fill="none" stroke="#fff" stroke-width="1.5"/></svg></div>
<h1 class="abs hero-title">BASED IN CAMBRIDGE,<br>ENGLAND.</h1>
<p class="abs hero-sub">Discovering &amp; developing<br>secondary uses for existing drugs</p>
<a class="abs btn hero-btn">More Details</a>
<div class="abs dots"><span class="on"></span><span></span><span></span></div>

<h2 class="abs mission-title">Mission</h2>
<p class="abs mission-text">Veltrora Ltd was established in 2008 to provide collaborative services to companies seeking expert advice in the area novel uses for existing drugs, or 'drug repurposing'.</p>

<section class="abs feature track">
  <div class="photo" role="img" aria-label="Nurse with a patient in a wheelchair in a hospital corridor"></div>
  <h2 style="left:342px;top:22px">Track Record</h2>
  <p style="left:343px;top:45px;width:290px">Specifically, Veltrora has used drug repurposing to found and help to develop valuable intellectual property around clinical stage developments for various pharmaceutical and biotechnology companies in the following manner:</p>
  <a class="btn" style="position:absolute;left:342px;top:110px;width:103px;height:22px;line-height:22px">Click here</a>
</section>

<section class="abs feature services">
  <div class="photo" role="img" aria-label="Pile of assorted white, orange and green pills and capsules"></div>
  <h2 style="left:15px;top:22px">Services</h2>
  <p style="left:16px;top:45px;width:300px">Veltrora uses therapeutic switching to identify secondary uses for existing drugs in practically all areas.</p>
  <p style="left:16px;top:94px;width:300px">There are various types of collaborator that we work with:</p>
  <a class="btn" style="position:absolute;left:19px;top:118px;width:103px;height:22px;line-height:22px">Click here</a>
</section>

<aside class="abs book-box">
  <h3>New Book!</h3>
  <div class="book-cover" role="img" aria-label="Book cover"></div>
</aside>
<div class="abs reviews">
  <div class="review r1">Reviews: 'A fascinating read...lot more balanced and intellectually satisfying than the much higher profile Hollow Pills...essential reading',&nbsp;&nbsp;&nbsp;&nbsp;&nbsp;&nbsp;&nbsp; - <cite style="display:inline">Medicines Information Director, Regional Health Board</cite></div>
  <div class="review r2">Very interesting read and impressive fact-finding!',<cite>-&nbsp; Dept Head, Norvanta Pharma</cite></div>
  <div class="review r3">'I can thoroughly recommend the book. Lots of thought provoking information and ideas',<cite>-&nbsp; Drug Discovery expert, UK</cite></div>
</div>

<div class="abs social-bar">
  <div class="label">Get social with us <i></i><i></i></div>
  <div class="contact">Contact</div>
</div>
<footer class="abs site-footer">
  Terms of Use Veltrora Ltd 2008-2017.<br>
  Registered in England and Wales registration number 5814207. All rights reserved.
</footer>
</body>
</html>
```